Brivane - Business Cards for a new venture

create business card for a startup classified business dealing in construction materials, the cards need to have a professional look but modern, more serious than playful, one of the samples must include the official font (attached), please explore using the official colors in the company's logo

Target Market(s)

Energy sector

Contact Information for Business Card

Font styles to use
Other font styles liked:
• suissnord

Requirements
Must have
• corporate colors (in logo attached)
Nice to have
• Official font (in one of the samples) font is : suissnord
Should not have
• Cartoonish look

```html
<!DOCTYPE html>
<html lang="en">
<head>
<meta charset="utf-8">
<title>Brivane – Business Cards</title>
<link href="https://fonts.googleapis.com/css2?family=Raleway:wght@400;500;700&display=swap" rel="stylesheet">
<style>
  :root {
    --brand-blue: #0c4679;
    --brand-grey: #8f9297;
    --paper: #ffffff;
    --backdrop: #e8e6e3;
    --on-blue: #ffffff;
    --card-w: 520px;
    --card-h: 297px;
  }
  * { box-sizing: border-box; margin: 0; padding: 0; }
  html, body {
    width: 1200px; height: 997px; overflow: hidden;
    background: var(--backdrop);
    font-family: "Raleway", sans-serif;
  }
  .sheet {
    width: 1200px; height: 997px;
    display: flex; align-items: center; justify-content: center; gap: 40px;
  }
  .card {
    position: relative;
    width: var(--card-w); height: var(--card-h);
    overflow: hidden;
    box-shadow: 0 6px 18px rgba(0,0,0,.12);
  }

  /* Front */
  .card--front { background: var(--paper); }
  .card__panels { position: absolute; inset: 0; }
  .brand-block {
    position: absolute; left: 0; top: 70px; width: 240px;
    text-align: center;
  }
  .brand-mark {
    display: inline-block; width: 14px; height: 14px; border-radius: 50%;
    background: var(--brand-blue); margin-bottom: 14px;
  }
  .brand-name {
    display: block;
    font-size: 30px; font-weight: 500; letter-spacing: 5px;
    color: var(--brand-grey); text-transform: uppercase;
  }
  .website {
    position: absolute; left: 0; bottom: 32px; width: 270px; text-align: center;
    font-size: 14px; font-weight: 500; letter-spacing: .5px;
    color: var(--brand-blue);
  }
  .contact {
    position: absolute; left: 318px; top: 30px; right: 20px;
    color: var(--on-blue);
  }
  .contact__name { font-size: 15px; font-weight: 700; }
  .contact__role { font-size: 11px; margin-top: 2px; }
  .contact__address { font-size: 11px; line-height: 1.45; margin-top: 56px; }
  .contact__list { list-style: none; margin-top: 14px; font-size: 11px; line-height: 1.6; }
  .contact__list li { display: flex; align-items: center; gap: 6px; }
  .contact__list svg { width: 10px; height: 10px; flex: none; }

  /* Back */
  .card--back {
    background: var(--brand-blue);
    display: flex; flex-direction: column; align-items: center; justify-content: center;
  }
  .card--back .brand-mark { background: var(--on-blue); }
  .card--back .brand-name { color: var(--on-blue); font-size: 32px; }
</style>
</head>
<body>
<main class="sheet">

  <section class="card card--front" aria-label="Business card front">
    <svg class="card__panels" viewBox="0 0 520 297" width="520" height="297" aria-hidden="true">
      <polygon points="244,0 256,0 322,297 310,297" fill="var(--brand-grey)"/>
      <polygon points="252,0 520,0 520,297 318,297 268,76 276,62 262,48" fill="var(--brand-blue)"/>
    </svg>

    <div class="brand-block">
      <span class="brand-mark"></span>
      <span class="brand-name">Brivane</span>
    </div>
    <p class="website">www.brivane.com</p>

    <div class="contact">
      <p class="contact__name">Alden Pryce</p>
      <p class="contact__role">President</p>
      <p class="contact__address">Po. box 48 Harlow Road,<br>Eastmere, Zip Code - 40210</p>
      <ul class="contact__list">
        <li>
          <svg viewBox="0 0 10 10"><path d="M2 1l2 2-1 1.2c.6 1.2 1.5 2.1 2.8 2.8L7 6l2 2-1.2 1.4C4.5 9.2.8 5.5.6 2.2z" fill="currentColor"/></svg>
          (240) 318-0012
        </li>
        <li>
          <svg viewBox="0 0 10 10"><rect x="2.5" y=".5" width="5" height="9" rx="1" fill="none" stroke="currentColor"/></svg>
          (240) 318-0013
        </li>
        <li>
          <svg viewBox="0 0 10 10"><rect x=".5" y="2" width="9" height="6" fill="currentColor"/><path d="M.5 2L5 5.5 9.5 2" fill="none" stroke="var(--brand-blue)" stroke-width=".9"/></svg>
          info@brivane.com
        </li>
      </ul>
    </div>
  </section>

  <section class="card card--back" aria-label="Business card back">
    <span class="brand-mark"></span>
    <span class="brand-name">Brivane</span>
  </section>

</main>
</body>
</html>
```